Branding Website

Updated content for the website:
https://files.quorvel.net/d/7Kp_x3mQ9tRz2vLw85-bN6Yc1HsfGqj-/open?share=yes
About me: Please check my bio through my other website which is halvercastmedia.com.au. I'd like my personal branding website to be more interactive.
I've come up with a design (see attached powerpoint) It's basically the Vornix UI home page / landing page. Regarding the 'link in bio' I've incorporated it into this branding website. The word documents will have each square aka TV details.
Under the 'episode details' which is a small bio you'll see 2 icons;
1) Play
2) Bio
Play will be a 2 min video of my career to date.
Bio will just be my bio off halvercastmedia.com.au.
This site will be much more interactive than the previous one we've made (halvercastmedia.com.au). When you click video, I want the video to pop up (same as main longer bio)
Underneath this you will start to see the Sub Headings that 'mock' the different shows on Vornix. These will be a carousel that scrolls to the left and also enlarges as you hover over the square aka TV
The first Sub-Heading 1)
is my job summary. Company, Title, Location,Dates, Responsibilities and Awards as you click the section it will take you to that info. All of the information will be similar to a workvane profile. I've got the info for you. I just need to copy and paste it into a document from my WorkVANE profile.
Sub-heading 2) University | Certificates
I've made a start (see attached) but have a lot more to complete. I've sent you what I've completed (plovex certifications) to give you an idea of what I'm after. I have completed all of the certificates I just need to copy and paste the links into that document for Trelmark and the remainder. I'm sending it through for you to get an understanding.
Sub-Heading 3) Client Testimonials
This section is the only section that is 100% complete and finished (see attached)

```html
<!DOCTYPE html>
<html lang="en">
<head>
<meta charset="utf-8">
<title>Miles Halvercast — Personal Branding</title>
<link rel="stylesheet" href="https://fonts.googleapis.com/css2?family=Manrope:wght@400;500;600;700;800&display=swap">
<style>
  :root{
    --canvas:#ffffff;
    --hero-top:#1a2550;
    --hero-bottom:#212f5c;
    --section-bg:#11143f;
    --footer-bg:#0e1139;
    --divider:#1f2352;
    --grid-line:#1c2055;
    --text:#ffffff;
    --text-soft:#d7d9ea;
    --logo-grey:#7c809e;
    --accent:#7b2bf0;
    --accent-deep:#4a0e72;
    --accent-blue:#1f2a8c;
    --frame:#23232b;
  }
  *{box-sizing:border-box;margin:0;padding:0}
  html,body{width:1200px;height:1200px;overflow:hidden;background:var(--canvas)}
  body{font-family:"Manrope",Arial,sans-serif;color:var(--text);position:relative}

  .page{position:absolute;left:217px;top:56px;width:774px;height:1060px;background:var(--section-bg);
        border-top:2px solid var(--frame);border-bottom:2px solid var(--frame);overflow:hidden}

  /* Hero */
  .hero{position:absolute;left:0;top:0;width:774px;height:402px;border-bottom-left-radius:26px;overflow:hidden;
        background:linear-gradient(135deg,var(--hero-top) 0%,#1e2b58 45%,#26335f 75%,#1c2750 100%)}
  .hero-backdrop{position:absolute;inset:0;
        background:radial-gradient(ellipse at 78% 40%,rgba(70,90,140,.35),transparent 60%),
                   radial-gradient(ellipse at 95% 20%,rgba(120,60,70,.18),transparent 50%)}
  .signature{position:absolute;left:87px;top:66px;width:205px;height:69px;border-radius:6px;
        background:linear-gradient(90deg,rgba(255,255,255,.10),rgba(255,255,255,.04))}
  .hero-title{position:absolute;left:87px;top:131px;font-size:25px;font-weight:700;letter-spacing:-.6px;white-space:nowrap}
  .hero-intro{position:absolute;left:87px;top:181px;width:245px;padding-left:10px;border-left:1px solid var(--text);
        font-size:8.2px;line-height:12.7px;font-weight:500;color:var(--text-soft);letter-spacing:-.15px}
  .hero-actions{position:absolute;left:90px;top:275px;display:flex;gap:3px}
  .btn{height:27px;background:#fff;color:#0b0b14;font-size:7px;font-weight:800;display:flex;align-items:center;justify-content:center;border-radius:1px}
  .btn-play{width:53px}
  .btn-bio{width:78px}
  .portrait{position:absolute;left:589px;top:78px;width:185px;height:324px;border-radius:60px 60px 0 0;
        background:linear-gradient(180deg,#c9a98a 0%,#b7a48c 30%,#a79a86 65%,#8a7c68 100%)}

  /* Carousel sections */
  .showcase{position:absolute;left:0;width:774px;height:92px;border-bottom:1px solid var(--divider)}
  .showcase-title{position:absolute;left:24px;top:19px;font-size:10.5px;font-weight:700;letter-spacing:-.2px}
  .carousel{position:absolute;left:0;top:62px;width:774px;height:20px}
  .carousel-arrow{position:absolute;top:0;width:19px;height:19px}
  .carousel-arrow.prev{left:153px}
  .carousel-arrow.next{left:617px}
  .brand{position:absolute;top:2px;transform:translateX(-50%);font-size:12px;font-weight:600;color:var(--logo-grey);letter-spacing:-.2px}

  /* Footer */
  .footer{position:absolute;left:0;top:769px;width:774px;height:291px;background:var(--footer-bg)}
  .grid-line{position:absolute;top:0;width:1px;height:291px;background:var(--grid-line)}
  .contact{position:absolute;left:87px;top:31px;font-size:7.4px;line-height:10px;color:var(--text-soft);font-weight:500}
  .contact h4{font-size:7.4px;font-weight:700;color:var(--text);margin-bottom:3px}
  .contact p{margin-bottom:13px}
  .location-map{position:absolute;left:564px;top:31px;width:122px;height:96px;
        background:linear-gradient(135deg,#e8ebf1,#d5dbe6)}
  .back-to-top{position:absolute;left:88px;top:162px;width:46px;height:48px}
  .peaks{position:absolute;left:0;top:0;width:774px;height:291px}
  .copyright{position:absolute;left:281px;top:252px;font-size:8.2px;color:var(--text-soft);white-space:nowrap}
  .copyright strong{color:var(--text);font-weight:600}
  .privacy{position:absolute;left:627px;top:252px;font-size:8.2px;color:var(--text-soft)}
</style>
</head>
<body>
<main class="page">

  <section class="hero">
    <div class="hero-backdrop" role="img" aria-label="Blurred wall of streaming show tiles"></div>
    <div class="signature" role="img" aria-label="Handwritten signature of Miles Halvercast"></div>
    <h1 class="hero-title">#1 in TV Shows Today</h1>
    <p class="hero-intro">Miles Halvercast is a dynamic media sales leader with 19 years of experience transforming traditional broadcast sales through digital innovation. Certified in Advanced TV Advertising technologies, he bridges traditional linear tv sales and emerging platforms with proven fiscal results, leadership and technological insight.</p>
    <div class="hero-actions">
      <span class="btn btn-play">PLAY</span>
      <span class="btn btn-bio">BIOGRAPHY</span>
    </div>
    <div class="portrait" role="img" aria-label="Portrait of Miles Halvercast in a beige three-piece suit"></div>
  </section>

  <section class="showcase" style="top:402px">
    <h2 class="showcase-title">Experience | Awards</h2>
    <div class="carousel">
      <svg class="carousel-arrow prev" viewBox="0 0 19 19"><circle cx="9.5" cy="9.5" r="9" fill="none" stroke="#2c3063"/><path d="M13 9.5H6M8.5 7L6 9.5 8.5 12" fill="none" stroke="#7b2bf0" stroke-width="1.1"/></svg>
      <span class="brand" style="left:239px">quillon</span>
      <span class="brand" style="left:343px">quillon</span>
      <span class="brand" style="left:447px">brisko</span>
      <span class="brand" style="left:551px">ZENTRO</span>
      <svg class="carousel-arrow next" viewBox="0 0 19 19"><circle cx="9.5" cy="9.5" r="9" fill="none" stroke="#2c3063"/><path d="M6 9.5H13M10.5 7L13 9.5 10.5 12" fill="none" stroke="#7b2bf0" stroke-width="1.1"/></svg>
    </div>
  </section>

  <section class="showcase" style="top:494px">
    <h2 class="showcase-title">University | Certificates</h2>
    <div class="carousel">
      <svg class="carousel-arrow prev" viewBox="0 0 19 19"><circle cx="9.5" cy="9.5" r="9" fill="none" stroke="#2c3063"/><path d="M13 9.5H6M8.5 7L6 9.5 8.5 12" fill="none" stroke="#7b2bf0" stroke-width="1.1"/></svg>
      <span class="brand" style="left:239px">quillon</span>
      <span class="brand" style="left:343px">quillon</span>
      <span class="brand" style="left:447px">brisko</span>
      <span class="brand" style="left:551px">ZENTRO</span>
      <svg class="carousel-arrow next" viewBox="0 0 19 19"><circle cx="9.5" cy="9.5" r="9" fill="none" stroke="#2c3063"/><path d="M6 9.5H13M10.5 7L13 9.5 10.5 12" fill="none" stroke="#7b2bf0" stroke-width="1.1"/></svg>
    </div>
  </section>

  <section class="showcase" style="top:586px">
    <h2 class="showcase-title">Client Testimonials</h2>
    <div class="carousel">
      <svg class="carousel-arrow prev" viewBox="0 0 19 19"><circle cx="9.5" cy="9.5" r="9" fill="none" stroke="#2c3063"/><path d="M13 9.5H6M8.5 7L6 9.5 8.5 12" fill="none" stroke="#7b2bf0" stroke-width="1.1"/></svg>
      <span class="brand" style="left:239px">quillon</span>
      <span class="brand" style="left:343px">quillon</span>
      <span class="brand" style="left:447px">brisko</span>
      <span class="brand" style="left:551px">ZENTRO</span>
      <svg class="carousel-arrow next" viewBox="0 0 19 19"><circle cx="9.5" cy="9.5" r="9" fill="none" stroke="#2c3063"/><path d="M6 9.5H13M10.5 7L13 9.5 10.5 12" fill="none" stroke="#7b2bf0" stroke-width="1.1"/></svg>
    </div>
  </section>

  <section class="showcase" style="top:677px">
    <h2 class="showcase-title">Blog</h2>
    <div class="carousel">
      <svg class="carousel-arrow prev" viewBox="0 0 19 19"><circle cx="9.5" cy="9.5" r="9" fill="none" stroke="#2c3063"/><path d="M13 9.5H6M8.5 7L6 9.5 8.5 12" fill="none" stroke="#7b2bf0" stroke-width="1.1"/></svg>
      <span class="brand" style="left:239px">quillon</span>
      <span class="brand" style="left:343px">quillon</span>
      <span class="brand" style="left:447px">brisko</span>
      <span class="brand" style="left:551px">ZENTRO</span>
      <svg class="carousel-arrow next" viewBox="0 0 19 19"><circle cx="9.5" cy="9.5" r="9" fill="none" stroke="#2c3063"/><path d="M6 9.5H13M10.5 7L13 9.5 10.5 12" fill="none" stroke="#7b2bf0" stroke-width="1.1"/></svg>
    </div>
  </section>

  <footer class="footer">
    <svg class="peaks" viewBox="0 0 774 291" aria-hidden="true">
      <defs>
        <linearGradient id="peakBlue" x1="0" y1="0" x2="1" y2="1">
          <stop offset="0" stop-color="#2a1a86"/>
          <stop offset="1" stop-color="#1e2a8e"/>
        </linearGradient>
      </defs>
      <polygon points="87.5,250 161,177 235,250 235,291 87.5,291" fill="#4a0e72"/>
      <polygon points="176,250 249,177 322,250 322,291 176,291" fill="url(#peakBlue)"/>
    </svg>
    <span class="grid-line" style="left:155px"></span>
    <span class="grid-line" style="left:311px"></span>
    <span class="grid-line" style="left:467px"></span>
    <span class="grid-line" style="left:624px"></span>

    <div class="contact">
      <h4>Contact Us</h4>
      <p>hello@mileshalvercast.com.au</p>
      <p>+61 03 9127 4460</p>
      <p>Workvane.au/miles-<br>halvercast</p>
      <p>Friendloop.com/<br>halvercastmedia.com</p>
    </div>

    <div class="location-map" role="img" aria-label="Street map showing the Halvercast Media office in the city centre"></div>

    <svg class="back-to-top" viewBox="0 0 46 48" aria-label="Back to top">
      <defs>
        <linearGradient id="arrowGrad" x1="0" y1="0" x2="0" y2="1">
          <stop offset="0" stop-color="#9b2cf5"/>
          <stop offset="1" stop-color="#3c2ee0"/>
        </linearGradient>
      </defs>
      <path d="M23 47V4M2 25L23 4 44 25" fill="none" stroke="url(#arrowGrad)" stroke-width="4.5"/>
    </svg>

    <p class="copyright">©2024 <strong>Miles Halvercast.</strong> All Rights Reserved.</p>
    <p class="privacy">Privacy Policy</p>
  </footer>

</main>
</body>
</html>
```